The Orchard of Virtue Customized for my Business

Hi! I am interested in getting some design ideas to take this Orchard of Virtue and put a bit of branding of my business into it. Open to any and all designs, this is intended to put on a 20"x24" or 16"x20" canvas so I can have it in my office for team training purposes. I have included a picture of the wall this canvas will go on. Thank you!

```html
<!DOCTYPE html>
<html lang="en">
<head>
<meta charset="utf-8">
<title>Orchard of Virtue — Millbrook</title>
<link rel="stylesheet" href="https://fonts.googleapis.com/css2?family=Merriweather:wght@700;900&family=Montserrat:wght@700;800&family=PT+Sans+Narrow:wght@400;700&display=swap">
<style>
  :root {
    --slate: #5b5b5b;
    --slate-dark: #4a4a4a;
    --sky: #3fb6ec;
    --sky-deep: #2fa6dc;
    --white: #ffffff;
    --ink: #1c1c1c;
  }
  html, body { margin: 0; padding: 0; overflow: hidden; }
  .poster {
    position: relative;
    width: 1200px;
    height: 950px;
    overflow: hidden;
    background: var(--slate);
  }
  .poster-art { position: absolute; inset: 0; }
  .brand {
    position: absolute;
    top: 96px;
    left: 790px;
    width: 340px;
    display: flex;
    align-items: center;
    gap: 16px;
  }
  .brand-dot {
    width: 44px; height: 44px;
    border-radius: 50%;
    background: var(--sky);
    flex: none;
  }
  .brand-name {
    font-family: "Montserrat", sans-serif;
    font-weight: 800;
    font-size: 58px;
    color: var(--white);
    letter-spacing: -1px;
  }
  .block {
    position: absolute;
    background: var(--white);
    color: var(--ink);
    padding: 5px 6px 4px;
    box-sizing: border-box;
    overflow: hidden;
  }
  .block h3 {
    margin: 0 0 3px;
    font-family: "Merriweather", serif;
    font-weight: 900;
    font-size: 12.5px;
    line-height: 1.1;
    text-align: center;
    text-transform: uppercase;
  }
  .block p {
    margin: 0;
    font-family: "PT Sans Narrow", sans-serif;
    font-size: 9.6px;
    line-height: 1.12;
  }
  .block-peak h3 { font-size: 14px; }
  .side-label {
    font-family: "Merriweather", serif;
    font-weight: 900;
    font-size: 7.5px;
    fill: var(--ink);
    text-transform: uppercase;
  }
  .side-note {
    font-family: "PT Sans Narrow", sans-serif;
    font-size: 5px;
    fill: #444;
  }
  .title {
    font-family: "Montserrat", sans-serif;
    font-weight: 800;
    font-size: 44px;
    fill: var(--white);
    letter-spacing: 2px;
  }
  .site {
    position: absolute;
    left: 0; right: 0;
    top: 872px;
    text-align: center;
    font-family: "Montserrat", sans-serif;
    font-weight: 700;
    font-size: 27px;
    letter-spacing: 1.5px;
    color: var(--white);
  }
</style>
</head>
<body>
<main class="poster">
  <svg class="poster-art" width="1200" height="950" viewBox="0 0 1200 950" aria-hidden="true">
    <path class="wave" d="M0,575 C300,605 650,565 880,505 C1000,472 1100,442 1200,425 L1200,950 L0,950 Z" fill="var(--sky)"/>
    <polygon points="600,128 135,802 1065,802" fill="var(--slate-dark)"/>
    <polygon points="600,142 153,794 1047,794" fill="var(--white)"/>
    <polygon points="600,158 170,786 1030,786" fill="var(--sky)"/>

    <g class="side-cells" fill="var(--white)">
      <polygon points="585,190 597,190 597,272 529,272"/>
      <polygon points="603,190 615,190 671,272 603,272"/>
      <polygon points="523,280 529,280 529,366 464,366"/>
      <polygon points="671,280 677,280 736,366 671,366"/>
      <polygon points="459,374 464,374 464,448 408,448"/>
      <polygon points="734,374 741,374 792,448 734,448"/>
      <polygon points="402,456 409,456 409,530 351,530"/>
      <polygon points="791,456 798,456 849,530 791,530"/>
      <polygon points="346,538 354,538 354,612 295,612"/>
      <polygon points="846,538 854,538 905,612 846,612"/>
      <polygon points="290,620 292,620 292,694 239,694"/>
      <polygon points="908,620 910,620 961,694 908,694"/>
    </g>

    <g transform="translate(580,240) rotate(-55.5)"><text class="side-label" text-anchor="middle">Hope</text><text class="side-note" y="7" text-anchor="middle">(looking ahead)</text></g>
    <g transform="translate(621,236) rotate(55.5)"><text class="side-label" text-anchor="middle">Grace</text><text class="side-note" y="7" text-anchor="middle">(kind manner)</text></g>
    <g transform="translate(513,333) rotate(-55.5)"><text class="side-label" text-anchor="middle">Grit</text><text class="side-note" y="7" text-anchor="middle">(steady effort)</text></g>
    <g transform="translate(688,328) rotate(55.5)"><text class="side-label" text-anchor="middle">Candor</text><text class="side-note" y="7" text-anchor="middle">(plain speech)</text></g>
    <g transform="translate(450,413) rotate(-55.5)"><text class="side-label" text-anchor="middle">Ingenuity</text><text class="side-note" y="7" text-anchor="middle">(clever thinking)</text></g>
    <g transform="translate(750,410) rotate(55.5)"><text class="side-label" text-anchor="middle">Constancy</text><text class="side-note" y="7" text-anchor="middle">(earns trust)</text></g>
    <g transform="translate(392,495) rotate(-55.5)"><text class="side-label" text-anchor="middle">Flexibility</text><text class="side-note" y="7" text-anchor="middle">(bending well)</text></g>
    <g transform="translate(808,494) rotate(55.5)"><text class="side-label" text-anchor="middle">Truth</text><text class="side-note" y="7" text-anchor="middle">(honest deeds)</text></g>
    <g transform="translate(336,578) rotate(-55.5)"><text class="side-label" text-anchor="middle">Aspiration</text><text class="side-note" y="7" text-anchor="middle">(high aims)</text></g>
    <g transform="translate(864,576) rotate(55.5)"><text class="side-label" text-anchor="middle">Warmth</text><text class="side-note" y="7" text-anchor="middle">(toward others)</text></g>

    <polygon class="title-band" points="233,702 967,702 1015,772 185,772" fill="var(--white)"/>
    <polygon class="title-bar" points="246,711 954,711 987,764 213,764" fill="var(--sky-deep)"/>
    <text class="title" x="600" y="754" text-anchor="middle">ORCHARD OF VIRTUE</text>
  </svg>

  <div class="brand">
    <span class="brand-dot"></span>
    <span class="brand-name">millbrook</span>
  </div>

  <section class="orchard-blocks">
    <div class="block block-peak" style="left:535px;top:280px;width:130px;height:86px">
      <h3>Full Bloom</h3>
      <p>Rising to meet the moment when it matters most, and relishing the hardest tests the season brings.</p>
    </div>

    <div class="block" style="left:470px;top:374px;width:126px;height:74px">
      <h3>Calm</h3>
      <p>Staying steady and true to yourself, at ease whatever the day brings.</p>
    </div>
    <div class="block" style="left:602px;top:374px;width:126px;height:74px">
      <h3>Assurance</h3>
      <p>Quiet belief earned through preparation and a clear view of what truly counts.</p>
    </div>

    <div class="block" style="left:415px;top:456px;width:120px;height:74px">
      <h3>Fitness</h3>
      <p>Care for body and mind alike. Sleep well, move often and eat with balance.</p>
    </div>
    <div class="block" style="left:541px;top:456px;width:116px;height:74px">
      <h3>Craft</h3>
      <p>Mastery of the basics, practiced until they come quickly and well.</p>
    </div>
    <div class="block" style="left:663px;top:456px;width:122px;height:74px">
      <h3>Unity</h3>
      <p>Putting the group first and sharing credit freely so everyone can grow.</p>
    </div>

    <div class="block" style="left:360px;top:538px;width:115px;height:74px">
      <h3>Composure</h3>
      <p>Keep feelings in check and let sound judgment guide each choice.</p>
    </div>
    <div class="block" style="left:481px;top:538px;width:115px;height:74px">
      <h3>Attention</h3>
      <p>Notice the details, stay curious and look for ways to get better.</p>
    </div>
    <div class="block" style="left:602px;top:538px;width:115px;height:74px">
      <h3>Drive</h3>
      <p>Step forward without waiting to be asked. Treat mistakes as lessons.</p>
    </div>
    <div class="block" style="left:723px;top:538px;width:117px;height:74px">
      <h3>Focus</h3>
      <p>Pick a clear target and hold to it, steady through every distraction.</p>
    </div>

    <div class="block" style="left:298px;top:620px;width:115px;height:74px">
      <h3>Diligence</h3>
      <p>Good outcomes grow from steady effort and thoughtful planning each day.</p>
    </div>
    <div class="block" style="left:419px;top:620px;width:116px;height:74px">
      <h3>Kinship</h3>
      <p>Built on shared respect and care, and tended by both sides over time.</p>
    </div>
    <div class="block" style="left:541px;top:620px;width:116px;height:74px">
      <h3>Devotion</h3>
      <p>Stand by the people who count on you, and keep your own respect.</p>
    </div>
    <div class="block" style="left:663px;top:620px;width:116px;height:74px">
      <h3>Harmony</h3>
      <p>Work well with everyone. Listen first and seek the best path together.</p>
    </div>
    <div class="block" style="left:785px;top:620px;width:117px;height:74px">
      <h3>Zeal</h3>
      <p>Energy that spreads to those around you. Love the work you do.</p>
    </div>
  </section>

  <div class="site">WWW.MILLBROOKHEALTH.COM</div>
</main>
</body>
</html>
```